Vergleichsportal für Reparaturen benötigt Flyer-Design
Zielgruppe
Wir sind ein Vergleichsportal für Reparaturen. Auf unserem Portal können sich Reparaturwerkstätten anmelden und deren Dienstleistungen mit Preisen hinterlegen. Der Kunde wählt das zu reparierende Gerät aus und gibt seine Adresse ein. Anschließend bekommt der Kunde alle Werkstätten nach Entfernung zum Kunden angezeigt mit den Reparaturpreisen. Der Kunde wählt seine Werkstatt aus und bezahlt den Reparaturpreis direkt auf unseren Portal. Die Zahlung geht auf ein Treuhandkonto. Der Kunde gibt das Gerät an die ausgewählt Werkstatt ab und erst wenn der Kunde mit der Reparatur zufrieden war, wird der Reparaturbetrag an die Werkstatt vom Kunden freigegeben.
Unsere Zielgruppe sind Kunden im Alter von 18 bis 40 Jahren und Technikaffine. Darunter Qualitätsbewusste Kunde sowie Schnäppchenjäger. Unsere Webseite lautet: flickwerkstube.de
Aufgabenstellung
Das Design sollte ansprechend sein und Interesse beim Kunden wecken. Die Farbe sollte unserer Webseite entsprechen. Es können auch Elemente von der Webseite übernommen werden wie z. B. die Vergleichseite etc.
Auf der Vorderseite sollte die Vorteile abgebildet werden.
- Finde deine Werkstatt in deiner Nähe
- Vergleiche die Qualität und Preise der Werkstätten
- Online Best Preis sichern und lokal reparieren lassen
- Abgesichert durch den Kaufhort Siegel Käuferschutz
- Sichere Zahlung über MUNDOR Treuhandschutz
Noch ein Call To Action/Störer einbauen. 'Jetzt Gutschein nutzen und sparen'
Auf der Rückseite sollte Gutscheine bzw. Coupons abgebildet sein.
ca. 6 Gutscheine mit unterschiedlichen Angeboten.
z. B. Displayreparatur
Velkor Modelle
10 Euro
Gutscheincode
Weiterhin sollte die Siegel drauf sein. Gerne auf beiden Seiten. Und ganz unten auf der Rückseite sollte Platz für den Rechtstext sein.
Gerne können eigene Idee mit einfließen.
Ich freue mich auf deinen Flyer.
Vielen DANK im Voraus

```html
<!DOCTYPE html>
<html lang="de">
<head>
<meta charset="utf-8">
<title>flickwerkstube – Flyer Vorder- und Rückseite</title>
<link href="https://fonts.googleapis.com/css2?family=Montserrat:wght@400;500;600;700;800&display=swap" rel="stylesheet">
<style>
  :root{
    --green:#8dc63f;
    --green-dark:#76ad2c;
    --teal:#1f4d59;
    --ink:#2a3a40;
    --band:#eef0f0;
    --page:#dcdedf;
    --white:#ffffff;
  }
  *{box-sizing:border-box;margin:0;padding:0}
  html,body{width:750px;height:1200px;overflow:hidden}
  body{background:var(--page);font-family:'Montserrat',sans-serif;color:var(--ink);position:relative}

  .flyer{position:absolute;top:237px;width:417px;height:890px;background:var(--white);
    transform:scale(.815);transform-origin:top left;overflow:hidden;box-shadow:0 2px 8px rgba(0,0,0,.12)}
  .flyer--front{left:25px}
  .flyer--back{left:385px}
  .abs{position:absolute}

  /* front */
  .top-bar{left:0;top:0;width:100%;height:8px;background:var(--green)}
  .side-strip{left:0;top:8px;width:30px;height:842px;background:var(--teal)}
  .hero-bg{left:30px;top:8px;width:387px;height:240px;background:linear-gradient(90deg,#f4f5f2 0%,#eef0ea 38%,#e9d9c8 55%,#d9643a 78%,#e07a4a 100%)}
  .hero-photo{left:190px;top:8px;width:227px;height:240px;background:radial-gradient(ellipse at 45% 35%,#e8c3a4 0%,#d98c5e 35%,#e2532e 70%,#f08a55 100%);opacity:.9}
  .brand{font-family:'Montserrat',sans-serif;font-weight:600;color:var(--teal);display:flex;align-items:center;gap:8px}
  .brand-dot{width:14px;height:14px;border-radius:50%;background:var(--green);flex:none}
  .flyer--front .brand{left:48px;top:48px;font-size:28px}
  .tagline{left:30px;height:30px;background:var(--white);border:1.5px solid var(--green);border-left:none;
    font-weight:700;font-size:15px;line-height:27px;color:var(--teal);padding:0 0 0 16px;
    letter-spacing:-.3px;white-space:nowrap}
  .tagline--1{top:128px;width:242px}
  .tagline--2{top:168px;width:190px}
  .tagline--near{left:70px;top:206px;font-weight:700;font-size:16px;color:var(--green);letter-spacing:1.5px;white-space:nowrap}

  .promo{left:262px;top:200px;width:124px;height:124px;border-radius:50%;background:var(--white);border:2px solid var(--green);padding:6px}
  .promo-inner{width:100%;height:100%;border-radius:50%;background:var(--green);color:var(--white);
    display:flex;flex-direction:column;align-items:center;justify-content:center;text-align:center;
    font-weight:600;font-size:12px;line-height:1.15;transform:rotate(-12deg)}
  .promo-inner b{font-size:20px;font-weight:600;margin-bottom:4px}

  .box-title{border:2px solid var(--green);font-weight:700;font-size:20px;color:var(--teal);padding:3px 8px;background:var(--white);white-space:nowrap}
  .vorteile-title{left:82px;top:268px}

  .benefit{left:0;width:417px;height:80px}
  .benefit--band{background:linear-gradient(90deg,transparent 0,transparent 40px,var(--band) 40px)}
  .benefit-icon{position:absolute;left:13px;top:14px;width:50px;height:50px;border-radius:50%;background:var(--white);
    border:2px solid var(--green);display:flex;align-items:center;justify-content:center}
  .benefit-title{position:absolute;left:84px;top:22px;font-weight:700;font-size:16px;color:var(--green);white-space:nowrap}
  .benefit-text{position:absolute;left:84px;top:42px;font-size:12px;color:var(--ink);white-space:nowrap;letter-spacing:-.1px}

  .repair-band{left:30px;top:700px;width:387px;height:150px;background:var(--band)}
  .repair-title{left:82px;top:710px}
  .device{top:764px;width:46px;height:46px;border-radius:50%;background:var(--white);border:2px solid var(--green);
    display:flex;align-items:center;justify-content:center}

  .bottom-bar{left:0;top:850px;width:100%;height:40px;background:var(--green)}
  .seal{border-radius:50%;background:#2d3436;border:3px solid var(--white);box-shadow:0 0 0 1px #999}
  .seal--light{background:var(--white);border:3px solid var(--teal);box-shadow:none}
  .front-url{right:16px;top:862px;color:var(--white);font-weight:600;font-size:14px;white-space:nowrap}

  /* back */
  .top-bar--teal{background:var(--teal)}
  .flyer--back .brand{left:100px;top:58px;font-size:28px}
  .coupons-title{left:95px;top:132px;width:225px;text-align:center;font-size:25px;padding:4px 0}
  .intro{left:20px;top:194px;width:377px;text-align:center;font-size:8.5px;line-height:1.3;color:var(--ink)}

  .coupon{position:absolute;width:175px;height:85px;border:1.5px solid var(--teal);border-radius:3px;background:var(--white)}
  .coupon-disc{position:absolute;left:-10px;top:-10px;width:78px;height:78px;border-radius:50%;background:var(--green);
    color:var(--white);display:flex;flex-direction:column;align-items:center;justify-content:center;line-height:1}
  .disc-amount{font-weight:700;font-size:27px}
  .disc-label{font-weight:600;font-size:14px;margin-top:1px}
  .coupon-offer{position:absolute;left:72px;top:10px;width:100px;text-align:center;font-weight:700;font-size:11px;line-height:1.15;color:var(--teal);white-space:nowrap}
  .coupon-code{position:absolute;left:72px;top:52px;width:100px;text-align:center;font-size:10.5px;color:var(--green-dark);line-height:1.25}
  .coupon-code small{display:block;font-size:7.5px;color:var(--ink)}
  .coupon-cut{position:absolute;left:8px;bottom:2px}
  .cut-line{left:0;width:417px;border-top:1.5px dashed #9aa4a6}

  .url-bar{left:92px;top:796px;width:235px;height:26px;background:var(--teal);color:var(--white);font-weight:600;font-size:12.5px;
    display:flex;align-items:center;justify-content:center;white-space:nowrap}
  .contact{top:838px;display:flex;align-items:center;gap:6px;font-size:9.5px;line-height:1.2;color:var(--ink);white-space:nowrap}
  .contact svg{flex:none}
  .bottom-bar--thin{top:876px;height:14px}
</style>
</head>
<body>

<!-- Vorderseite -->
<section class="flyer flyer--front">
  <div class="abs top-bar"></div>
  <div class="abs hero-bg"></div>
  <div class="abs hero-photo" role="img" aria-label="Foto: lachende Frau am Telefon zeigt Daumen hoch"></div>
  <div class="abs side-strip"></div>

  <div class="abs brand"><span class="brand-dot"></span>flickwerkstube</div>

  <div class="abs tagline tagline--1">DAS VERGLEICHSPORTAL</div>
  <div class="abs tagline tagline--2">FÜR REPARATUREN</div>
  <div class="abs tagline--near">IN DEINER NÄHE</div>

  <div class="abs promo"><div class="promo-inner"><b>%</b>GUTSCHEINE<br>NUTZEN UND<br>SPAREN!</div></div>

  <div class="abs box-title vorteile-title">VORTEILE</div>

  <div class="abs benefit" style="top:318px">
    <div class="benefit-icon"><svg width="26" height="26" viewBox="0 0 24 24" fill="none" stroke="#8dc63f" stroke-width="1.8"><path d="M12 21s-6-6.2-6-11a6 6 0 0 1 12 0c0 4.8-6 11-6 11z"/><circle cx="12" cy="10" r="2.2"/><path d="M6 21h12"/></svg></div>
    <div class="benefit-title">KUNDENNÄHE</div>
    <div class="benefit-text">Finde eine Werkstatt in deiner Nähe</div>
  </div>
  <div class="abs benefit benefit--band" style="top:398px">
    <div class="benefit-icon"><svg width="24" height="26" viewBox="0 0 24 24" fill="none" stroke="#8dc63f" stroke-width="1.8"><rect x="6" y="3" width="13" height="17" rx="1.5"/><path d="M4 6v15h12M9 8h7M9 11h7M9 14h5"/></svg></div>
    <div class="benefit-title">VERGLEICH</div>
    <div class="benefit-text">Vergleiche Qualität und Preise der Werkstätten</div>
  </div>
  <div class="abs benefit" style="top:478px">
    <div class="benefit-icon"><svg width="28" height="24" viewBox="0 0 28 24" fill="none" stroke="#8dc63f" stroke-width="1.8"><ellipse cx="14" cy="13" rx="9" ry="7"/><path d="M9 19v3M19 19v3M23 12h3M12 6h4"/><circle cx="18" cy="11" r=".8" fill="#8dc63f"/></svg></div>
    <div class="benefit-title">BEST PRICE</div>
    <div class="benefit-text">Online Best Price sichern &amp; lokal reparieren lassen</div>
  </div>
  <div class="abs benefit benefit--band" style="top:558px">
    <div class="benefit-icon"><svg width="26" height="26" viewBox="0 0 24 24" fill="none" stroke="#8dc63f" stroke-width="1.8"><path d="M12 3l7 3v6c0 4.5-3 7.5-7 9-4-1.5-7-4.5-7-9V6z"/><path d="M9 7.5c-1 1-1.5 2.5-1.5 4"/></svg></div>
    <div class="benefit-title">SICHERE ABWICKLUNG</div>
    <div class="benefit-text">Abgesichert durch den Kaufhort Siegel Käuferschutz</div>
  </div>
  <div class="abs benefit" style="top:638px">
    <div class="benefit-icon"><svg width="26" height="26" viewBox="0 0 24 24" fill="none" stroke="#8dc63f" stroke-width="1.8"><path d="M12 3l7 3v6c0 4.5-3 7.5-7 9-4-1.5-7-4.5-7-9V6z"/><circle cx="12" cy="12" r="3.5"/><path d="M10 11h3M10 13h3"/></svg></div>
    <div class="benefit-title">SICHERE ZAHLUNG</div>
    <div class="benefit-text">Sichere Bezahlung über MUNDOR Treuhandschutz</div>
  </div>

  <div class="abs repair-band"></div>
  <div class="abs box-title repair-title">REPARATUREN</div>

  <div class="abs device" style="left:57px"><svg width="20" height="24" viewBox="0 0 20 24" fill="none" stroke="#1f4d59" stroke-width="2"><rect x="5" y="2" width="10" height="20" rx="2"/><path d="M9 18h2"/></svg></div>
  <div class="abs device" style="left:117px"><svg width="24" height="24" viewBox="0 0 24 24" fill="none" stroke="#1f4d59" stroke-width="2"><rect x="3" y="4" width="18" height="16" rx="2"/><path d="M11 17h2"/></svg></div>
  <div class="abs device" style="left:177px"><svg width="26" height="24" viewBox="0 0 26 24" fill="none" stroke="#1f4d59" stroke-width="2"><rect x="2" y="4" width="6" height="16"/><rect x="10" y="4" width="14" height="10"/><path d="M17 14v4M13 19h8"/></svg></div>
  <div class="abs device" style="left:237px"><svg width="26" height="22" viewBox="0 0 26 22" fill="none" stroke="#1f4d59" stroke-width="2"><rect x="5" y="3" width="16" height="11" rx="1"/><path d="M2 17h22"/></svg></div>
  <div class="abs device" style="left:297px"><svg width="20" height="26" viewBox="0 0 20 26" fill="none" stroke="#1f4d59" stroke-width="2"><rect x="4" y="6" width="12" height="14" rx="3"/><path d="M6 6V2h8v4M6 20v4h8v-4"/></svg></div>
  <div class="abs device" style="left:357px"><svg width="28" height="20" viewBox="0 0 28 20" fill="none" stroke="#1f4d59" stroke-width="2"><path d="M7 3h14c3 0 5 5 5 10 0 4-3 5-5 2l-2-3H9l-2 3c-2 3-5 2-5-2C2 8 4 3 7 3z"/><path d="M8 7v5M5.5 9.5h5"/><circle cx="19" cy="8" r="1" fill="#1f4d59"/><circle cx="21" cy="11" r="1" fill="#1f4d59"/></svg></div>

  <div class="abs bottom-bar"></div>
  <div class="abs seal" style="left:58px;top:830px;width:50px;height:50px"></div>
  <div class="abs seal seal--light" style="left:118px;top:830px;width:50px;height:50px"></div>
  <div class="abs front-url">WWW.FLICKWERKSTUBE.DE</div>
</section>

<!-- Rückseite -->
<section class="flyer flyer--back">
  <div class="abs top-bar top-bar--teal"></div>
  <div class="abs brand"><span class="brand-dot"></span>flickwerkstube</div>

  <div class="abs box-title coupons-title">GUTSCHEINE:</div>
  <p class="abs intro">Lorem ipsum dolor sit amet, consetetur sadipscing elitr, sed diam nonumy eirmod tempor invidunt ut labore et dolore magna aliquyam erat, sed diam voluptua.</p>

  <div class="coupon" style="left:22px;top:262px">
    <div class="coupon-disc"><span class="disc-amount">10€</span><span class="disc-label">RABATT</span></div>
    <div class="coupon-offer">AUF DISPLAY<br>REPARATUREN</div>
    <div class="coupon-code"><small>Gutscheincode:</small>10XMaiX2019</div>
    <svg class="coupon-cut" width="16" height="12" viewBox="0 0 16 12" fill="none" stroke="#1f4d59" stroke-width="1.2"><circle cx="3" cy="3" r="2"/><circle cx="3" cy="9" r="2"/><path d="M5 4l10 5M5 8l10-5"/></svg>
  </div>
  <div class="coupon" style="left:225px;top:262px">
    <div class="coupon-disc"><span class="disc-amount">10%</span><span class="disc-label">RABATT</span></div>
    <div class="coupon-offer">AUF DISPLAY<br>REPARATUREN</div>
    <div class="coupon-code"><small>Gutscheincode:</small>10XMaiX2019</div>
    <svg class="coupon-cut" width="16" height="12" viewBox="0 0 16 12" fill="none" stroke="#1f4d59" stroke-width="1.2"><circle cx="3" cy="3" r="2"/><circle cx="3" cy="9" r="2"/><path d="M5 4l10 5M5 8l10-5"/></svg>
  </div>

  <div class="abs cut-line" style="top:382px"></div>

  <div class="coupon" style="left:22px;top:418px">
    <div class="coupon-disc"><span class="disc-amount">10%</span><span class="disc-label">RABATT</span></div>
    <div class="coupon-offer">AUF VELKOR<br>MODELLE</div>
    <div class="coupon-code"><small>Gutscheincode:</small>10XMaiX2019</div>
    <svg class="coupon-cut" width="16" height="12" viewBox="0 0 16 12" fill="none" stroke="#1f4d59" stroke-width="1.2"><circle cx="3" cy="3" r="2"/><circle cx="3" cy="9" r="2"/><path d="M5 4l10 5M5 8l10-5"/></svg>
  </div>
  <div class="coupon" style="left:225px;top:418px">
    <div class="coupon-disc"><span class="disc-amount">10€</span><span class="disc-label">RABATT</span></div>
    <div class="coupon-offer">AUF DISPLAY<br>REPARATUREN</div>
    <div class="coupon-code"><small>Gutscheincode:</small>10XMaiX2019</div>
    <svg class="coupon-cut" width="16" height="12" viewBox="0 0 16 12" fill="none" stroke="#1f4d59" stroke-width="1.2"><circle cx="3" cy="3" r="2"/><circle cx="3" cy="9" r="2"/><path d="M5 4l10 5M5 8l10-5"/></svg>
  </div>

  <div class="abs cut-line" style="top:541px"></div>

  <div class="coupon" style="left:22px;top:582px">
    <div class="coupon-disc"><span class="disc-amount">10€</span><span class="disc-label">RABATT</span></div>
    <div class="coupon-offer">AUF DISPLAY<br>REPARATUREN</div>
    <div class="coupon-code"><small>Gutscheincode:</small>10XMaiX2019</div>
    <svg class="coupon-cut" width="16" height="12" viewBox="0 0 16 12" fill="none" stroke="#1f4d59" stroke-width="1.2"><circle cx="3" cy="3" r="2"/><circle cx="3" cy="9" r="2"/><path d="M5 4l10 5M5 8l10-5"/></svg>
  </div>
  <div class="coupon" style="left:225px;top:582px">
    <div class="coupon-disc"><span class="disc-amount">10%</span><span class="disc-label">RABATT</span></div>
    <div class="coupon-offer">AUF DISPLAY<br>REPARATUREN</div>
    <div class="coupon-code"><small>Gutscheincode:</small>10XMaiX2019</div>
    <svg class="coupon-cut" width="16" height="12" viewBox="0 0 16 12" fill="none" stroke="#1f4d59" stroke-width="1.2"><circle cx="3" cy="3" r="2"/><circle cx="3" cy="9" r="2"/><path d="M5 4l10 5M5 8l10-5"/></svg>
  </div>

  <div class="abs seal" style="left:117px;top:702px;width:78px;height:78px"></div>
  <div class="abs seal seal--light" style="left:217px;top:702px;width:78px;height:78px"></div>

  <div class="abs url-bar">WWW.FLICKWERKSTUBE.DE</div>

  <div class="abs contact" style="left:30px">
    <svg width="20" height="20" viewBox="0 0 24 24" fill="none" stroke="#8dc63f" stroke-width="1.8"><circle cx="12" cy="12" r="10.5"/><path d="M12 18s-4-4-4-7a4 4 0 0 1 8 0c0 3-4 7-4 7z"/></svg>
    <span>Lindenweg 12<br>80331 Musterstadt</span>
  </div>
  <div class="abs contact" style="left:152px">
    <svg width="20" height="20" viewBox="0 0 24 24" fill="none" stroke="#8dc63f" stroke-width="1.8"><circle cx="12" cy="12" r="10.5"/><path d="M8 7l2-1 1.5 3-1.3 1c.6 1.5 1.8 2.7 3.3 3.3l1-1.3 3 1.5-1 2c-4 0-8.5-4.5-8.5-8.5z"/></svg>
    <span>Telefon:<br>089 555012340</span>
  </div>
  <div class="abs contact" style="left:265px">
    <svg width="20" height="20" viewBox="0 0 24 24" fill="none" stroke="#8dc63f" stroke-width="1.8"><circle cx="12" cy="12" r="10.5"/><rect x="6.5" y="8" width="11" height="8"/><path d="M6.5 8l5.5 4.5L17.5 8"/></svg>
    <span>E-Mail:<br>info@flickwerkstube.de</span>
  </div>

  <div class="abs bottom-bar bottom-bar--thin"></div>
</section>

</body>
</html>
```